New label design for Vitmain Water beverage

This is to create a new label for a vitamin water company called Zelbo Vitamin. The label should be in dual languages. English and Arabic as seen attached for a previous example. You do not have to create an Arabic logo, just make space for it and I will have someon else do it. If you think you can do it, go ahead. I have also attached the bottle dimensions we are thinking of using. Please provide a new bottle design if you see fit. Please remember the bottle size is 400ml, and no pressure If I don't get a great bottle design, then I will use the attached one in that case. Please make the label diverse for various flavors, so it would apply easily and color print friendly. The brand is healthy, sporty, low or no sugars, no artificial flavors and no artificial coloring. All vitamins, minirals and electrolytes are healthy and real. Three flavors: pomogranite cherry, tropical citrus, and kiwi strawberry. So, each label would have different vitamins and offers unique components. Make it hip, trendy yet classy.
Good Luck!!!
Updates

Target Market(s)

Age 15-40 males and females

Industry/Entity Type

Water Company

Requirements
Nice to have
• Plastic PET bottle design
• a 500 ml version

```html
<!DOCTYPE html>
<html lang="en">
<head>
<meta charset="utf-8">
<title>Zelbo Vitamin – Flavour Labels</title>
<link rel="stylesheet" href="https://fonts.googleapis.com/css2?family=Titillium+Web:wght@300;400;600;700&display=swap">
<style>
  :root {
    --page: #ffffff;
    --silver-light: #fbfbfc;
    --silver-mid: #e4e5e8;
    --silver-dark: #b9bbc0;
    --ink-grey: #4a4a4f;
    --navy: #1c2a6e;
    --white: #ffffff;
    --kiwi-strawberry: #e97ccc;
    --kiwi-strawberry-deep: #d65bb6;
    --pomegranate-cherry: #c8232c;
    --pomegranate-cherry-deep: #8e1a20;
    --tropical-citrus: #f4a423;
    --tropical-citrus-deep: #e08a12;
  }
  * { box-sizing: border-box; margin: 0; padding: 0; }
  html, body {
    width: 1200px; height: 985px; overflow: hidden;
    background: var(--page);
    font-family: "Titillium Web", sans-serif;
  }
  .label-range {
    width: 1200px; height: 985px;
    display: flex; justify-content: center; align-items: center; gap: 50px;
  }
  .label {
    --flavour: var(--kiwi-strawberry);
    --flavour-deep: var(--kiwi-strawberry-deep);
    position: relative;
    width: 340px; height: 470px;
    background: linear-gradient(90deg, var(--silver-mid) 0%, var(--silver-light) 35%, var(--white) 55%, var(--silver-mid) 100%);
    box-shadow: 0 0 0 1px #dcdde0;
    overflow: hidden;
  }
  .label--pomegranate { --flavour: var(--pomegranate-cherry); --flavour-deep: var(--pomegranate-cherry-deep); }
  .label--citrus { --flavour: var(--tropical-citrus); --flavour-deep: var(--tropical-citrus-deep); }

  .natural-badge {
    position: absolute; top: 22px; left: 14px;
    width: 62px; height: 50px;
    background: var(--flavour);
    border-radius: 0 0 12px 0;
    color: var(--white);
    text-align: center;
    font-weight: 700; line-height: 1;
    padding-top: 8px;
  }
  .natural-badge .pct { display: block; font-size: 19px; }
  .natural-badge .word { display: block; font-size: 11px; letter-spacing: .3px; margin-top: 2px; }

  .brand-name {
    position: absolute; top: 58px; left: 0; right: 0;
    text-align: center;
    color: var(--flavour);
    font-weight: 600;
    line-height: .9;
  }
  .brand-name .main { display: block; font-size: 82px; letter-spacing: -1px; }
  .brand-name .sub { display: block; font-size: 46px; margin-top: 4px; }

  .flavour-bar {
    position: absolute; top: 208px; left: 42px; right: 42px;
    background: var(--navy);
    border: 3px solid var(--white);
    outline: 2px solid var(--navy);
    color: var(--white);
    text-align: center;
    font-size: 21px; font-weight: 600; letter-spacing: .5px;
    line-height: 30px;
    text-transform: uppercase;
  }

  .chevron-band { position: absolute; top: 262px; left: 0; width: 340px; height: 40px; }

  .flavour-panel {
    position: absolute; top: 282px; left: 0; right: 0; bottom: 0;
    background: radial-gradient(ellipse at 30% 30%, var(--flavour) 0%, var(--flavour) 45%, var(--flavour-deep) 100%);
    clip-path: polygon(0 0, 40% 0, 50% 22px, 60% 0, 100% 0, 100% 100%, 0 100%);
    color: var(--white);
  }
  .claims {
    position: absolute; top: 50px; left: 22px; right: 22px;
    list-style: none;
    font-size: 13px; font-weight: 600; letter-spacing: .2px;
    line-height: 1.55;
    text-transform: uppercase;
  }
  .claims li { display: inline; }
  .claims li::before { content: "• "; }
  .claims li + li { margin-left: 4px; }
  .volume {
    position: absolute; right: 20px; bottom: 62px;
    font-size: 17px; font-weight: 400;
  }
</style>
</head>
<body>
<main class="label-range">

  <section class="label label--kiwi" aria-label="Kiwi Strawberry label">
    <div class="natural-badge"><span class="pct">100%</span><span class="word">NATURAL</span></div>
    <h2 class="brand-name"><span class="main">Zelbo</span><span class="sub">Vitamin</span></h2>
    <p class="flavour-bar">Kiwi Strawberry</p>
    <svg class="chevron-band" viewBox="0 0 340 40" aria-hidden="true">
      <polygon points="0,8 130,8 170,30 210,8 340,8 340,20 210,20 170,40 130,20 0,20" fill="#c4c6cb"/>
      <polygon points="0,12 132,12 170,33 208,12 340,12 340,16 208,16 170,37 132,16 0,16" fill="#f4f4f6"/>
    </svg>
    <div class="flavour-panel">
      <ul class="claims"><li>No sugars</li><li>No artificial flavors and</li><li>No artificial coloring</li></ul>
      <span class="volume">400ml</span>
    </div>
  </section>

  <section class="label label--pomegranate" aria-label="Pomegranate Cherry label">
    <div class="natural-badge"><span class="pct">100%</span><span class="word">NATURAL</span></div>
    <h2 class="brand-name"><span class="main">Zelbo</span><span class="sub">Vitamin</span></h2>
    <p class="flavour-bar">Pomogranite Cherry</p>
    <svg class="chevron-band" viewBox="0 0 340 40" aria-hidden="true">
      <polygon points="0,8 130,8 170,30 210,8 340,8 340,20 210,20 170,40 130,20 0,20" fill="#c4c6cb"/>
      <polygon points="0,12 132,12 170,33 208,12 340,12 340,16 208,16 170,37 132,16 0,16" fill="#f4f4f6"/>
    </svg>
    <div class="flavour-panel">
      <ul class="claims"><li>No sugars</li><li>No artificial flavors and</li><li>No artificial coloring</li></ul>
      <span class="volume">400ml</span>
    </div>
  </section>

  <section class="label label--citrus" aria-label="Tropical Citrus label">
    <div class="natural-badge"><span class="pct">100%</span><span class="word">NATURAL</span></div>
    <h2 class="brand-name"><span class="main">Zelbo</span><span class="sub">Vitamin</span></h2>
    <p class="flavour-bar">Tropical Citrus</p>
    <svg class="chevron-band" viewBox="0 0 340 40" aria-hidden="true">
      <polygon points="0,8 130,8 170,30 210,8 340,8 340,20 210,20 170,40 130,20 0,20" fill="#c4c6cb"/>
      <polygon points="0,12 132,12 170,33 208,12 340,12 340,16 208,16 170,37 132,16 0,16" fill="#f4f4f6"/>
    </svg>
    <div class="flavour-panel">
      <ul class="claims"><li>No sugars</li><li>No artificial flavors and</li><li>No artificial coloring</li></ul>
      <span class="volume">400ml</span>
    </div>
  </section>

</main>
</body>
</html>
```